Brindle Works - Fast, Efficient and Gas Mainteance for Domestic, Commercial and Industrial clients

We are in the process of purchasing a new business and would like to get a new logo and business card.
Business is a gas maintenance business that also does new gas installations.
Has been established since 1988.
Services include:
Install all types of gas appliances & equipment inc. hot water units
Maintain / repair / replace all types of gas appliances & equipment

Target Market(s)

Domestic, Commercial and Industrial clients

Industry/Entity Type

Business

Contact Information for Business Card

admin@brindleworks-example.com.au
07 5981 4726
Brindle Works PTY LTD

Logo Text

Gas Fitting & Plumbing Maintenance Specialists

Font styles to use
Sans Serif

Requirements
Must have
• Logo
• Business name, contact number, email address, web address
• Domestic | Commercial | Industrial Est Since 1988
Nice to have
• Possibly a black card with a flame logo to one side
Should not have
• Spelling errors

```html
<!DOCTYPE html>
<html lang="en">
<head>
<meta charset="utf-8">
<title>Brindle Works PTY LTD – Business Card</title>
<link rel="stylesheet" href="https://fonts.googleapis.com/css2?family=PT+Sans:wght@400;700&display=swap">
<style>
  :root {
    --canvas-grey: #d0d0d0;
    --card-black: #000000;
    --brand-yellow: #f7d10f;
    --brand-orange: #f29420;
    --sub-orange: #e07a22;
    --back-top: #f4cb22;
    --back-bottom: #ef7c22;
    --text-white: #ffffff;
    --icon-orange: #f4a21a;
  }
  * { margin: 0; padding: 0; box-sizing: border-box; }
  html, body {
    width: 1200px;
    height: 900px;
    overflow: hidden;
    background: var(--canvas-grey);
    font-family: "PT Sans", "Helvetica Neue", Arial, sans-serif;
  }
  .canvas {
    position: relative;
    width: 1200px;
    height: 900px;
  }
  .card {
    position: absolute;
    top: 200px;
    width: 310px;
    height: 502px;
    overflow: hidden;
  }
  .card-front {
    left: 265px;
    background: var(--card-black);
    border-radius: 62px 0 62px 0;
    color: var(--text-white);
  }
  .card-back {
    left: 641px;
    width: 309px;
    background: linear-gradient(180deg, var(--back-top) 0%, var(--brand-orange) 60%, var(--back-bottom) 100%);
    border-radius: 0 66px 0 66px;
  }

  /* front: wordmark */
  .brand-dot {
    position: absolute;
    left: 156px;
    top: 62px;
    width: 46px;
    height: 46px;
    border-radius: 50%;
    background: var(--brand-orange);
  }
  .wordmark {
    position: absolute;
    left: 56px;
    right: 0;
    text-align: center;
    white-space: nowrap;
    line-height: 1;
  }
  .wordmark-name {
    top: 182px;
    font-size: 28px;
    font-weight: 700;
    letter-spacing: 1px;
    color: var(--brand-yellow);
  }
  .wordmark-sub {
    top: 220px;
    font-size: 14px;
    font-weight: 400;
    letter-spacing: 3px;
    color: var(--sub-orange);
  }

  /* front: contact block */
  .address {
    position: absolute;
    left: 32px;
    top: 286px;
    font-size: 14px;
    line-height: 21px;
    font-style: normal;
  }
  .contact-list {
    position: absolute;
    left: 32px;
    top: 354px;
    list-style: none;
    font-size: 14px;
    line-height: 21px;
  }
  .contact-list li {
    display: flex;
    align-items: center;
    gap: 8px;
    white-space: nowrap;
  }
  .contact-list svg {
    width: 11px;
    height: 11px;
    flex: none;
    fill: var(--icon-orange);
  }
  .tagline {
    position: absolute;
    left: 32px;
    top: 434px;
    font-size: 15.5px;
    line-height: 21px;
    font-weight: 700;
  }
  .tagline .sectors { color: var(--brand-orange); }
  .tagline .since { color: var(--brand-yellow); }

  /* back: wordmark */
  .back-wordmark {
    position: absolute;
    left: 34px;
    color: var(--text-white);
    white-space: nowrap;
    line-height: 1;
  }
  .back-name { top: 40px; font-size: 30px; font-weight: 700; letter-spacing: 1px; }
  .back-sub  { top: 82px; font-size: 15px; font-weight: 400; letter-spacing: 3px; }
</style>
</head>
<body>
<main class="canvas">
  <section class="card card-front" aria-label="Business card front">
    <span class="brand-dot" aria-hidden="true"></span>
    <div class="wordmark wordmark-name">BRINDLE WORKS</div>
    <div class="wordmark wordmark-sub">PTY LTD</div>

    <address class="address">
      12345, Address Goes Here<br>
      Country Name, 123456
    </address>

    <ul class="contact-list">
      <li>
        <svg viewBox="0 0 24 24" aria-hidden="true"><path d="M6.6 10.8a15.1 15.1 0 0 0 6.6 6.6l2.2-2.2a1 1 0 0 1 1-.25 11.4 11.4 0 0 0 3.6.57 1 1 0 0 1 1 1V20a1 1 0 0 1-1 1A17 17 0 0 1 3 4a1 1 0 0 1 1-1h3.5a1 1 0 0 1 1 1c0 1.25.2 2.45.57 3.57a1 1 0 0 1-.25 1z"/></svg>
        <span>07 5981 4726</span>
      </li>
      <li>
        <svg viewBox="0 0 24 24" aria-hidden="true"><path d="M2 5h20v14H2z M2 5l10 8 10-8" /></svg>
        <span>admin@brindleworks-example.com.au</span>
      </li>
      <li>
        <svg viewBox="0 0 24 24" aria-hidden="true" style="fill:none;stroke:var(--icon-orange);stroke-width:3"><path d="M10 14a4 4 0 0 0 5.7 0l4-4a4 4 0 0 0-5.7-5.7l-1 1M14 10a4 4 0 0 0-5.7 0l-4 4a4 4 0 0 0 5.7 5.7l1-1"/></svg>
        <span>www.brindleworks-example.com.au</span>
      </li>
    </ul>

    <p class="tagline">
      <span class="sectors">Domestic | Commercial |</span><br>
      <span class="since">Industrial Est Since 1988</span>
    </p>
  </section>

  <section class="card card-back" aria-label="Business card back">
    <div class="back-wordmark back-name">BRINDLE WORKS</div>
    <div class="back-wordmark back-sub">PTY LTD</div>
  </section>
</main>
</body>
</html>
```